E-Commerce Custom Design Magento Standard Requirements For Marketing Agency

I need to revamp theme for a website www.plinthwavestudio.com and want to change name to www.plinthwavehomes.com I have logo attached. I need a custom e commerce website built that pops and grabs attention. My logo is silver and looks great on black background. Please just use all same content from existing website www.plinthwavestudio.com and use existing products that you see there.

Target Market(s)

REAL ESTATE AGENTS

Industry/Entity Type

Digital Marketing

Coding

Coded - Design and coding required

Number of Pages Required

5+ page

Colors

Designer to choose colors to be used in the design.

Requirements
Must have
• Please revamp entire website www.plinthwavestudio.com and use new logo attached. Domain name will be www.plinthwavehomes.com and will offer marketing services for real estate agents around the country and world. Specializing in digital marketing services such as Vellumly Ads, Pictoraze Ads, Quip Loop Ads, Zarbit Promoworks, Etc.
Nice to have
Should not have

```html
<!DOCTYPE html>
<html lang="en">
<head>
<meta charset="utf-8">
<title>Plinthwave Homes – Advanced Marketing Services</title>
<link rel="stylesheet" href="https://fonts.googleapis.com/css2?family=Montserrat:wght@400;500;600;700&family=Open+Sans:wght@400;600&display=swap">
<style>
:root{
  --ink:#1e1e1e;
  --text:#6f6f6f;
  --muted:#9a9a9a;
  --gold:#b8860b;
  --gold-dark:#9a6f07;
  --line:#e6e6e6;
  --btn-grey:#e4e4e4;
  --footer:#2d2d2d;
  --footer-line:#444;
  --white:#fff;
}
*{box-sizing:border-box;margin:0;padding:0}
html,body{width:1200px;height:3863px;overflow:hidden}
body{font-family:"Open Sans",Arial,sans-serif;color:var(--text);background:var(--white)}
h1,h2,h3,h4,.nav,.btn{font-family:Montserrat,Arial,sans-serif}

/* Hero */
.hero{position:relative;height:613px;color:var(--white)}
.hero-photo{position:absolute;inset:0;background:
  radial-gradient(ellipse at 60% 35%,#3c4a63 0%,#1a2030 40%,#07090e 80%),#07090e}
.hero-photo::after{content:"";position:absolute;inset:0;background:linear-gradient(90deg,rgba(0,0,0,.55),rgba(0,0,0,.1) 60%,rgba(0,0,0,.35))}
.topbar{position:relative;display:flex;align-items:center;justify-content:space-between;padding:24px 93px 0}
.brand{display:flex;align-items:center;gap:10px;font-family:Montserrat,sans-serif;font-weight:700;font-size:15px;letter-spacing:1px;color:#d8d8d8;text-transform:uppercase}
.brand-mark{width:26px;height:26px;border-radius:50%;background:#cfcfcf}
.nav{display:flex;align-items:center;gap:42px;font-size:12px;font-weight:500}
.nav a{color:var(--white);text-decoration:none}
.cart{position:relative;display:flex}
.cart-count{position:absolute;top:-6px;right:-8px;width:12px;height:12px;border-radius:50%;background:var(--gold);font-size:8px;text-align:center;line-height:12px}
.nav .contact{border:1.5px solid var(--white);border-radius:20px;padding:8px 34px;font-size:11px;font-weight:600;letter-spacing:.5px}
.hero-copy{position:relative;padding:185px 0 0 95px}
.hero-copy h2{font-weight:400;font-size:30px;letter-spacing:.3px}
.hero-copy h1{font-weight:700;font-size:41px;margin-top:6px;letter-spacing:.3px}
.btn-gold{display:inline-flex;align-items:center;gap:12px;margin-top:30px;background:var(--gold);color:var(--white);border-radius:24px;padding:12px 26px;font-size:10px;font-weight:600;letter-spacing:.5px}

/* Advantages */
.advantages{height:237px;border-bottom:1px solid var(--line);display:grid;grid-template-columns:repeat(4,250px);padding:83px 93px 0}
.adv{display:flex;gap:14px}
.adv svg{flex:none;margin-top:0}
.adv h3{font-size:14px;font-weight:500;color:var(--ink);margin-bottom:6px}
.adv p{font-size:10.5px;line-height:1.55;color:var(--muted)}

/* Services */
.services{height:2621px;padding:80px 93px 0}
.services h2{font-size:29px;font-weight:500;color:var(--ink);margin-bottom:37px}
.grid{display:grid;grid-template-columns:repeat(3,327px);column-gap:18px;row-gap:56px}
.card{height:428px;display:flex;flex-direction:column}
.card-photo{height:216px}
.card-body{flex:1;display:flex;flex-direction:column;border-bottom:1px solid var(--line);padding:24px 0 0}
.card h3{font-size:13.5px;font-weight:500;color:var(--ink);line-height:1.45;margin-bottom:10px}
.card p{font-size:9.5px;line-height:1.75;color:var(--muted)}
.buy{margin-top:auto;padding-bottom:22px;display:flex;align-items:flex-end;gap:22px}
.price s{display:block;font-size:9.5px;color:var(--muted)}
.price b{display:block;font-family:Montserrat,sans-serif;font-size:13px;font-weight:500;color:var(--gold-dark)}
.btn-cart{background:var(--btn-grey);color:var(--ink);font-size:8.5px;font-weight:600;letter-spacing:.5px;padding:10px 20px;border-radius:2px}

/* Footer */
.footer{height:392px;background:var(--footer);color:#c9c9c9;padding:78px 93px 0;position:relative}
.footer-top{display:flex}
.footer .brand{width:396px;align-self:flex-start;margin-top:8px}
.footer h4{font-size:11px;font-weight:700;color:var(--white);letter-spacing:.5px;margin-bottom:22px}
.footer-lists{display:grid;grid-template-columns:312px 312px}
.footer ul{list-style:none}
.footer li{font-size:10px;line-height:25.5px}
.footer-bottom{position:absolute;left:93px;right:93px;top:301px;border-top:1px solid var(--footer-line);padding-top:28px;display:flex;justify-content:space-between;font-size:10px;color:var(--muted)}
.footer-bottom strong{color:var(--white);font-weight:600}
.socials{display:flex;gap:14px}
.socials span{width:9px;height:9px;border-radius:50%;background:#9a9a9a}
</style>
</head>
<body>

<header class="hero">
  <div class="hero-photo" role="img" aria-label="Modern luxury home lit up at night with stone steps and garden"></div>
  <div class="topbar">
    <div class="brand"><span class="brand-mark"></span>Plinthwave</div>
    <nav class="nav">
      <a href="#">Products</a>
      <a href="#">About</a>
      <a href="#">Login</a>
      <span class="cart">
        <svg width="14" height="13" viewBox="0 0 14 13" fill="none" stroke="#fff" stroke-width="1.3"><path d="M1 1h2l2 8h7l1.5-6H4"/><circle cx="6" cy="11.5" r="1"/><circle cx="11" cy="11.5" r="1"/></svg>
        <span class="cart-count">0</span>
      </span>
      <a href="#" class="contact">CONTACT</a>
    </nav>
  </div>
  <div class="hero-copy">
    <h2>Advanced Marketing Services</h2>
    <h1>For The Plinthwave Realtor</h1>
    <span class="btn btn-gold">VIEW SERVICES
      <svg width="14" height="8" viewBox="0 0 14 8" fill="none" stroke="#fff" stroke-width="1.3"><path d="M0 4h13M9.5 .5 13 4 9.5 7.5"/></svg>
    </span>
  </div>
</header>

<section class="advantages">
  <div class="adv">
    <svg width="26" height="24" viewBox="0 0 26 24" fill="none" stroke="#b8860b" stroke-width="1.4"><path d="M2 12 13 2l11 10M5 9.5V22h16V9.5M10 22v-7h6v7"/></svg>
    <div><h3>Your advantage 01</h3><p>Clear local reach for every<br>listing, tuned to buyers near<br>your open house.</p></div>
  </div>
  <div class="adv">
    <svg width="26" height="24" viewBox="0 0 26 24" fill="none" stroke="#b8860b" stroke-width="1.4"><circle cx="13" cy="10" r="8"/><path d="M13 5v10M10 8h5a2 2 0 0 1 0 4h-4M8 22h10"/></svg>
    <div><h3>Your advantage 02</h3><p>Flat pricing with no hidden<br>fees and simple checkout<br>for each campaign.</p></div>
  </div>
  <div class="adv">
    <svg width="26" height="24" viewBox="0 0 26 24" fill="none" stroke="#b8860b" stroke-width="1.4"><path d="M3 20 9 8l5 7 4-5 5 10zM9 3v3M4 5l2 2M14 5l-2 2"/></svg>
    <div><h3>Your advantage 03</h3><p>Fast launch within days, run<br>by a team that knows real<br>estate marketing.</p></div>
  </div>
  <div class="adv">
    <svg width="26" height="24" viewBox="0 0 26 24" fill="none" stroke="#b8860b" stroke-width="1.4"><path d="M4 4h18v12H4zM9 20h8M13 16v4M8 12l3-3 2 2 4-4"/></svg>
    <div><h3>Your advantage 04</h3><p>Plain reports after every<br>campaign so you can see<br>the results you paid for.</p></div>
  </div>
</section>

<main class="services">
  <h2>Our Services</h2>
  <div class="grid">

    <article class="card">
      <div class="card-photo" role="img" aria-label="Smiling woman holding a smartphone" style="background:linear-gradient(135deg,#c9b9a6,#7d6a58)"></div>
      <div class="card-body">
        <h3>Plinthwave Social Growth Engine</h3>
        <p>We will create new, fresh, relevant social media content for your business and post it daily to your Pictoraze and Vellumly business pages FOR YOU. We also guarantee hundreds of new followers (not ghost followers) to your Pictoraze page every month.</p>
        <div class="buy"><div class="price"><s>$549.00</s><b>$249.00</b></div><span class="btn-cart">ADD TO CART</span></div>
      </div>
    </article>

    <article class="card">
      <div class="card-photo" role="img" aria-label="Hands typing on a laptop showing a social feed" style="background:linear-gradient(135deg,#8c8a86,#3c3a37)"></div>
      <div class="card-body">
        <h3>Vellumly Ad For One Open Hous</h3>
        <p>We will run an Vellumly Ad targeted to all residents in the neighborhood and surrounding neighborhood of your open house.</p>
        <div class="buy"><div class="price"><s>$549.00</s><b>$249.00</b></div><span class="btn-cart">ADD TO CART</span></div>
      </div>
    </article>

    <article class="card">
      <div class="card-photo" role="img" aria-label="Woman talking on a mobile phone outdoors" style="background:linear-gradient(135deg,#e9ecef,#a4a9ad)"></div>
      <div class="card-body">
        <h3>Voice Broadcast Marketing For One Open House</h3>
        <p>Leave up to 500 voicemails to residents in the neighborhood and surrounding neighborhood of your open house informing them of your open house.</p>
        <div class="buy"><div class="price"><s>$549.00</s><b>$249.00</b></div><span class="btn-cart">ADD TO CART</span></div>
      </div>
    </article>

    <article class="card">
      <div class="card-photo" role="img" aria-label="Team at a desk with phones and charts" style="background:linear-gradient(135deg,#f2f1ee,#b9b3a8)"></div>
      <div class="card-body">
        <h3>SMS Marketing For One Open House</h3>
        <p>Send up to 500 text messages to residents in the neighborhood and surrounding neighborhood of your open house informing them of your open house.</p>
        <div class="buy"><div class="price"><s>$549.00</s><b>$249.00</b></div><span class="btn-cart">ADD TO CART</span></div>
      </div>
    </article>

    <article class="card">
      <div class="card-photo" role="img" aria-label="Hands holding a smartphone above a laptop" style="background:linear-gradient(135deg,#d8d8d8,#5a5a5a)"></div>
      <div class="card-body">
        <h3>Pictoraze Ad For One Open House</h3>
        <p>We will run an Pictoraze Ad targeted to all residents in the neighborhood and surrounding neighborhood of your open house.</p>
        <div class="buy"><div class="price"><s>$549.00</s><b>$249.00</b></div><span class="btn-cart">ADD TO CART</span></div>
      </div>
    </article>

    <article class="card">
      <div class="card-photo" role="img" aria-label="Hand holding a phone with app icons" style="background:linear-gradient(135deg,#6b5c52,#1f1a17)"></div>
      <div class="card-body">
        <h3>Vellumly &amp; Pictoraze Ad Combo For One Open House</h3>
        <p>We will run a Vellumly and Pictoraze Ad targeted to all residents in the neighborhood and surrounding neighborhood of your open house.</p>
        <div class="buy"><div class="price"><s>$549.00</s><b>$249.00</b></div><span class="btn-cart">ADD TO CART</span></div>
      </div>
    </article>

    <article class="card">
      <div class="card-photo" role="img" aria-label="Person working on a laptop at a desk" style="background:linear-gradient(135deg,#7a756e,#2c2a27)"></div>
      <div class="card-body">
        <h3>Email Marketing For One Open House</h3>
        <p>Send up to 500 text messages to residents in the neighborhood and surrounding neighborhood of your open house informing them of your open house.</p>
        <div class="buy"><div class="price"><s>$549.00</s><b>$249.00</b></div><span class="btn-cart">ADD TO CART</span></div>
      </div>
    </article>

    <article class="card">
      <div class="card-photo" role="img" aria-label="Hands on a laptop beside a cup of coffee" style="background:linear-gradient(135deg,#f4f4f2,#bdbab4)"></div>
      <div class="card-body">
        <h3>Email &amp; SMS &amp; VB Marketing Combo For One Open House</h3>
        <p>Send up to 1000 text messages, voicemails and emails (up to 500 of each) to residents in the neighborhood and surrounding neighborhood of your open house.</p>
        <div class="buy"><div class="price"><s>$549.00</s><b>$249.00</b></div><span class="btn-cart">ADD TO CART</span></div>
      </div>
    </article>

    <article class="card">
      <div class="card-photo" role="img" aria-label="Presenter speaking to a small team in an office" style="background:linear-gradient(135deg,#3e4a4a,#121616)"></div>
      <div class="card-body">
        <h3>All Marketing Services For One Ipen House</h3>
        <p>Send up to 1500 text messages, voicemails and emails (up to 500 of each) to residents in the neighborhood and surrounding neighborhood of your open house.</p>
        <div class="buy"><div class="price"><s>$549.00</s><b>$249.00</b></div><span class="btn-cart">ADD TO CART</span></div>
      </div>
    </article>

    <article class="card">
      <div class="card-photo" role="img" aria-label="Hands with a notebook and laptop on a table" style="background:linear-gradient(135deg,#4a4744,#16140f)"></div>
      <div class="card-body">
        <h3>All Plinthwave Realtor Open House Marketing Services</h3>
        <p>Includes SMS, Voicemail Drops, Email Marketing, Vellumly &amp; Pictoraze Ads</p>
        <div class="buy"><div class="price"><s>$549.00</s><b>$249.00</b></div><span class="btn-cart">ADD TO CART</span></div>
      </div>
    </article>

    <article class="card">
      <div class="card-photo" role="img" aria-label="Phone resting on a laptop keyboard" style="background:linear-gradient(135deg,#b9b9b9,#4a4a4a)"></div>
      <div class="card-body">
        <h3>Vellumly Messenger Marketing Smart Social Connect</h3>
        <p>We Send Messages On Your Behalf Through Vellumly Messenger To All Customers That Have Engaged (Liked, Commented, Shared) With Your Vellumly Business Page or Posts (Paid &amp; Unpaid).</p>
        <div class="buy"><div class="price"><s>$549.00</s><b>$249.00</b></div><span class="btn-cart">ADD TO CART</span></div>
      </div>
    </article>

    <article class="card">
      <div class="card-photo" role="img" aria-label="Phone, notebook and pen on a white desk" style="background:linear-gradient(135deg,#f0efeb,#c8c4bc)"></div>
      <div class="card-body">
        <h3>Vellumly and Pictoraze Business Profiles Set Up</h3>
        <p>We Will Build A Vellumly &amp; Pictoraze Profile For Your Business and Deliver It in 3 days</p>
        <div class="buy"><div class="price"><s>$549.00</s><b>$249.00</b></div><span class="btn-cart">ADD TO CART</span></div>
      </div>
    </article>

    <article class="card">
      <div class="card-photo" role="img" aria-label="Keyboard key with network lines drawn around it" style="background:linear-gradient(135deg,#eceae4,#9b988f)"></div>
      <div class="card-body">
        <h3>Monthly Vellumly Marketing Management Fully Scalable Agency</h3>
        <p>Optimized For Lead Generation, New Sales and Repeat Business With Full Reporting, Laser Targeting – Full Vellumly Advertising Management.</p>
        <div class="buy"><div class="price"><s>$549.00</s><b>$249.00</b></div><span class="btn-cart">ADD TO CART</span></div>
      </div>
    </article>

    <article class="card">
      <div class="card-photo" role="img" aria-label="Laptop and coffee on a bright teal and orange desk" style="background:linear-gradient(135deg,#3f8a8f,#c7733c)"></div>
      <div class="card-body">
        <h3>Vellumly Remarketing Campaign</h3>
        <p>Remarket To Your Website Visitors and Your Current/Past Customers Right On Their Vellumly Newsfeeds.</p>
        <div class="buy"><div class="price"><s>$549.00</s><b>$249.00</b></div><span class="btn-cart">ADD TO CART</span></div>
      </div>
    </article>

  </div>
</main>

<footer class="footer">
  <div class="footer-top">
    <div class="brand"><span class="brand-mark"></span>Plinthwave</div>
    <div>
      <h4>SERVICES</h4>
      <div class="footer-lists">
        <ul>
          <li>Plinthwave social growth engine</li>
          <li>Vellumly ad for one open house</li>
          <li>Voice broadcast marketing for one open house</li>
          <li>SMS marketing for one open house</li>
          <li>Pictoraze ad for one open house</li>
          <li>Vellumly &amp; Pictoraze ad combo for one open house</li>
          <li>Email marketing for one open house</li>
        </ul>
        <ul>
          <li>Email &amp; SMS &amp; VB marketing combo for One open house</li>
          <li>All marketing services for one open house</li>
          <li>All Plinthwave realtor open house marketing services</li>
          <li>Vellumly messenger marketing smart social connect</li>
          <li>Vellumly and Pictoraze business profiles set up</li>
          <li>Monthly Vellumly marketing management</li>
          <li>Vellumly remarketing campaign</li>
        </ul>
      </div>
    </div>
  </div>
  <div class="footer-bottom">
    <span>© 2018 <strong>Plinthwave Realtor</strong> All Rights Reserved</span>
    <span class="socials"><span></span><span></span><span></span><span></span></span>
  </div>
</footer>

</body>
</html>
```